Etiketten-Design für Bier
Zielgruppe
Wie sind eine Brauerei und auch Limonadenhersteller. Zielgruppe sind alle Personen von 16-70.
Aufgabenstellung
In dieser Ausschreibung geht es um eine Etikettengarnitur (Hals- u. Bauchetikett) der Sorte PILS. Die komplette Serie mit Bieretiketten soll jedoch für alle 13 Biersorten neu erstellt werden. Der Gewinner erhält nach Verhandlung/Angebot ebenfalls alle weiteren Sorten. Wir könnten uns vorstellen, für alle Etikettenformate ein ähnliches Schema bzw. Grundgerüst zu verwenden. Sortenspezifisch wird dieses dann an die jeweilige Sorte angepasst. Es sollen nicht alle gleich aussehen und sich nur im Schriftzug unterscheiden. Es wäre zudem schön, wenn die sortentypischen Farben wieder in den neuen Etiketten aufgegriffen werden würden. Unsere Logo und der Slogan 'Leidenschaft Handwerk Qualität' sollte ebenfalls verwendet werden. Alle Stanzen (als Vektorgrafik), Formate, Beispiele, Texte sind im Upload zu finden. Aus Beispielen wie dem HELLES-Etikett können Logo usw. als Vektorgrafik entnommen werden.

```html
<!DOCTYPE html>
<html lang="de">
<head>
<meta charset="utf-8">
<title>Kellerhof – Etikettenserie</title>
<link rel="stylesheet" href="https://fonts.googleapis.com/css2?family=Roboto+Slab:wght@500&family=Kaushan+Script&family=UnifrakturMaguntia&family=Roboto+Condensed:ital,wght@0,400;1,400&display=swap">
<style>
  :root{
    --page:#f7f7f7;
    --band:#07070b;
    --paper:#f6f2e4;
    --stone-light:#d4d1cc;
    --stone-dark:#b3afaa;
    --ink:#141414;
    --pils:#5d7844;
    --pils-dark:#4a6236;
    --land:#b57a38;
    --land-dark:#8f5d27;
    --radler:#c4c21f;
    --radler-dark:#a6a418;
    --seal:#e4e2dc;
  }
  *{box-sizing:border-box;margin:0;padding:0}
  html,body{width:870px;height:1200px;overflow:hidden;background:var(--page)}
  .canvas{position:relative;width:870px;height:1200px;background:var(--page)}

  .variety{position:absolute;top:0;width:206px;height:997px}
  .variety--pils{left:78px;--tone:var(--pils);--tone-dark:var(--pils-dark)}
  .variety--landbier{left:327px;--tone:var(--land);--tone-dark:var(--land-dark)}
  .variety--radler{left:577px;--tone:var(--radler);--tone-dark:var(--radler-dark)}

  /* neck label */
  .neck{position:absolute;left:27px;top:262px;width:152px;height:160px}
  .neck__band{position:absolute;left:0;top:22px;width:152px;height:100px;
    background:linear-gradient(180deg,var(--stone-light),var(--stone-dark));
    clip-path:polygon(0 22%,50% 0,100% 22%,100% 62%,50% 100%,0 62%)}
  .neck__shield{position:absolute;left:32px;top:0;width:88px;height:150px}
  .neck__shield svg{position:absolute;inset:0}
  .neck__name{position:absolute;left:0;right:0;top:46px;text-align:center;
    font:500 14px/1 "Roboto Slab",serif;color:var(--ink)}
  .neck__sort{position:absolute;left:0;right:0;top:78px;text-align:center;
    font:18px/1 "Kaushan Script",cursive;color:var(--paper)}

  /* body label */
  .label{position:absolute;left:0;top:542px;width:206px;height:292px;overflow:hidden;
    background:linear-gradient(180deg,var(--stone-light),var(--stone-dark))}
  .label__field{position:absolute;inset:0;
    background:linear-gradient(180deg,var(--tone) 40%,var(--tone-dark));
    clip-path:polygon(0 43%,50% 20%,100% 30%,100% 100%,0 100%)}
  .label__shield{position:absolute;left:35px;top:10px;width:136px;height:180px}
  .label__shield svg{position:absolute;inset:0}
  .label__name{position:absolute;left:0;right:0;top:66px;text-align:center;
    font:500 22px/1 "Roboto Slab",serif;color:var(--ink)}
  .label__slogan{position:absolute;left:0;right:0;top:100px;text-align:center;
    font:10.5px/13px "UnifrakturMaguntia",serif;color:#3a3a3a}
  .label__seal{position:absolute;left:134px;top:138px;width:50px;height:50px;border-radius:50%;
    background:var(--seal);border:2px solid #8a8a8a}
  .label__sort{position:absolute;left:0;right:0;top:196px;text-align:center;
    font:36px/1 "Kaushan Script",cursive;color:var(--paper)}
  .label__abv{position:absolute;left:0;right:0;top:245px;text-align:center;
    font:italic 9px/1 "Roboto Condensed",sans-serif;color:var(--paper)}
  .label__volume{position:absolute;left:3px;top:259px;
    font:italic 12px/1 "Roboto Condensed",sans-serif;color:var(--paper);opacity:.85}
  .label__bbd{position:absolute;left:0;right:0;top:280px;text-align:center;
    font:6px/1 "Roboto Condensed",sans-serif;color:#222}

  /* brand band */
  .brand-band{position:absolute;left:0;top:997px;width:870px;height:203px;background:var(--band);
    display:flex;align-items:center;justify-content:center}
  .brand-band__name{font:500 40px/1 "Roboto Slab",serif;color:var(--paper)}
</style>
</head>
<body>
<main class="canvas">

  <section class="variety variety--pils" aria-label="Pils">
    <div class="neck">
      <div class="neck__band"></div>
      <div class="neck__shield">
        <svg viewBox="0 0 88 150" width="88" height="150">
          <path d="M2 30 Q2 2 44 2 Q86 2 86 30 V112 L44 148 L2 112 Z" fill="var(--paper)" stroke="var(--tone)" stroke-width="3"/>
          <path d="M2 72 H86 V112 L44 148 L2 112 Z" fill="var(--tone)"/>
        </svg>
        <div class="neck__name">Kellerhof</div>
        <div class="neck__sort">Pils</div>
      </div>
    </div>
    <div class="label">
      <div class="label__field" role="img" aria-label="Gezeichnete Hopfendolden auf grünem Grund"></div>
      <div class="label__shield">
        <svg viewBox="0 0 136 180" width="136" height="180">
          <path d="M3 42 Q3 3 68 3 Q133 3 133 42 V122 L68 177 L3 122 Z" fill="var(--paper)" stroke="var(--tone)" stroke-width="4"/>
        </svg>
        <div class="label__name">Kellerhof</div>
        <div class="label__slogan">Handwerk<br>Leidenschaft<br>Qualität</div>
      </div>
      <div class="label__seal"></div>
      <div class="label__sort">Pils</div>
      <div class="label__abv">Alk. 4,8% vol.</div>
      <div class="label__volume">0,5 l</div>
      <div class="label__bbd">Mindestens haltbar bis:</div>
    </div>
  </section>

  <section class="variety variety--landbier" aria-label="Landbier">
    <div class="neck">
      <div class="neck__band"></div>
      <div class="neck__shield">
        <svg viewBox="0 0 88 150" width="88" height="150">
          <path d="M2 30 Q2 2 44 2 Q86 2 86 30 V112 L44 148 L2 112 Z" fill="var(--paper)" stroke="var(--tone)" stroke-width="3"/>
          <path d="M2 72 H86 V112 L44 148 L2 112 Z" fill="var(--tone)"/>
        </svg>
        <div class="neck__name">Kellerhof</div>
        <div class="neck__sort">Landbier</div>
      </div>
    </div>
    <div class="label">
      <div class="label__field" role="img" aria-label="Gezeichnete Hügellandschaft auf braunem Grund"></div>
      <div class="label__shield">
        <svg viewBox="0 0 136 180" width="136" height="180">
          <path d="M3 42 Q3 3 68 3 Q133 3 133 42 V122 L68 177 L3 122 Z" fill="var(--paper)" stroke="var(--tone)" stroke-width="4"/>
        </svg>
        <div class="label__name">Kellerhof</div>
        <div class="label__slogan">Handwerk<br>Leidenschaft<br>Qualität</div>
      </div>
      <div class="label__seal"></div>
      <div class="label__sort">Landbier</div>
      <div class="label__abv">Alk. 4,8% vol.</div>
      <div class="label__volume">0,5 l</div>
      <div class="label__bbd">Mindestens haltbar bis:</div>
    </div>
  </section>

  <section class="variety variety--radler" aria-label="Radler">
    <div class="neck">
      <div class="neck__band"></div>
      <div class="neck__shield">
        <svg viewBox="0 0 88 150" width="88" height="150">
          <path d="M2 30 Q2 2 44 2 Q86 2 86 30 V112 L44 148 L2 112 Z" fill="var(--paper)" stroke="var(--tone)" stroke-width="3"/>
          <path d="M2 72 H86 V112 L44 148 L2 112 Z" fill="var(--tone)"/>
        </svg>
        <div class="neck__name">Kellerhof</div>
        <div class="neck__sort">Radler</div>
      </div>
    </div>
    <div class="label">
      <div class="label__field" role="img" aria-label="Gezeichnetes Fahrrad auf gelbgrünem Grund"></div>
      <div class="label__shield">
        <svg viewBox="0 0 136 180" width="136" height="180">
          <path d="M3 42 Q3 3 68 3 Q133 3 133 42 V122 L68 177 L3 122 Z" fill="var(--paper)" stroke="var(--tone)" stroke-width="4"/>
        </svg>
        <div class="label__name">Kellerhof</div>
        <div class="label__slogan">Handwerk<br>Leidenschaft<br>Qualität</div>
      </div>
      <div class="label__seal"></div>
      <div class="label__sort">Radler</div>
      <div class="label__abv">Alk. 4,8% vol.</div>
      <div class="label__volume">0,5 l</div>
      <div class="label__bbd">Mindestens haltbar bis:</div>
    </div>
  </section>

  <footer class="brand-band">
    <div class="brand-band__name">Kellerhof</div>
  </footer>

</main>
</body>
</html>
```